Mandala Postcard Design

I am in need of a postcard to hand out at a Psychic Fair. I envision the card to having half-of-a Mandala (from my Facebook folder), touched up a bit to make it vibrant and bold. Others vendors will have cards w/photographic backgrounds doing yoga. I'd like mine to stand out for it's line-drawn "cartoonish" nature, solid-color nature. The wording would be my basic contact info and a short description ... something like: "Experience the Magic of Mandala Making ... Next Class will be held: (open space for writing, no lines) The art is contained in this Facebook folder. Lots to choose from, with my favorites being the stronger outlined designs.

https://www.sketchnook.example/Brightloom/media_set?set=a.20262926615637197.2184852941.783542196&type=3
Updates

I just uploaded a few new drawings that might work better, since they are more round. I want to minimize the white space, for instance, avoid having the left & right corners empty. Another idea could be to use 1/4 mandalas in the corners. I'm ready to make a decision. I want it to look great, but as I gain drawing experience, I'll need to update my cards. Thanks! I'm not sure if this the place for this comment, but I'll also be needing a DVD label for my tutorials, and a front page design for a mandala coloring book.

Target Market(s)

Primarily women interested in metaphysical, psychic, meditation, reiki and a basic interest in art.

Font styles to use
Serif
Sans Serif

Requirements
Should not have
• Should not be on a dark card, really should be a plain white background, it seems, in order to stand out.

```html
<!DOCTYPE html>
<html lang="en">
<head>
<meta charset="utf-8">
<title>Mandala Making Postcard</title>
<link href="https://fonts.googleapis.com/css2?family=Josefin+Sans:wght@300;400;600;700&family=Patrick+Hand&display=swap" rel="stylesheet">
<style>
  :root {
    --sheet: #000000;
    --card: #ffffff;
    --ink: #1a1a1a;
    --rule: #2a2a2a;
    --faint: #e6e6e6;
    --faint-line: #cfcfcf;
    --warm-1: #f7a21b;
    --warm-2: #e8473f;
    --cool-1: #2fae84;
    --cool-2: #4c7cc8;
    --lilac: #b7a3b8;
  }
  * { box-sizing: border-box; margin: 0; padding: 0; }
  html, body {
    width: 776px;
    height: 1200px;
    overflow: hidden;
    background: var(--sheet);
  }
  .sheet { position: relative; width: 776px; height: 1200px; }
  .postcard {
    position: absolute;
    left: 34px;
    width: 710px;
    background: var(--card);
    overflow: hidden;
    color: var(--ink);
    font-family: "Josefin Sans", Arial, sans-serif;
  }
  .postcard--front { top: 24px; height: 564px; }
  .postcard--back { top: 618px; height: 550px; }

  .title { position: absolute; left: 24px; line-height: 1; }
  .title__lead { display: block; font-weight: 700; font-size: 28px; letter-spacing: 0.5px; }
  .title__mid { display: block; font-weight: 300; font-size: 25px; letter-spacing: 0.8px; margin-top: 9px; }
  .title__name { display: block; font-weight: 300; font-size: 39px; letter-spacing: 1px; margin-top: 9px; }
  .title__flourish { display: block; margin-top: 8px; }

  .front-title { top: 40px; }
  .back-title { top: 274px; }

  .class-note {
    position: absolute;
    left: 26px;
    top: 204px;
    width: 290px;
    height: 300px;
  }
  .class-note__label {
    position: absolute;
    left: 22px;
    top: 16px;
    font-family: "Patrick Hand", "Comic Sans MS", cursive;
    font-size: 19px;
  }

  .web {
    position: absolute;
    left: 24px;
    font-weight: 600;
    font-size: 17px;
    letter-spacing: 0.3px;
  }
  .front-web { top: 530px; }
  .visit {
    position: absolute;
    left: 24px;
    top: 478px;
    font-weight: 700;
    font-size: 21px;
    letter-spacing: 1px;
  }
  .back-web { top: 510px; }

  .art { position: absolute; }
  .art--mandala-half { right: 0; top: 0; width: 300px; height: 564px; }
  .art--mandala-faint { left: 0; top: 0; width: 370px; height: 230px; }
  .art--mandala-corner { right: 0; top: 312px; width: 90px; height: 190px; }

  .stamp {
    position: absolute;
    left: 599px;
    top: 34px;
    width: 76px;
    height: 102px;
    border: 1.5px solid var(--rule);
    border-radius: 9px;
  }
  .address-line {
    position: absolute;
    left: 524px;
    width: 150px;
    border-top: 1.5px solid var(--rule);
  }
</style>
</head>
<body>
<div class="sheet">

  <section class="postcard postcard--front">
    <h1 class="title front-title">
      <span class="title__lead">EXPERIENCE THE MAGIC</span>
      <span class="title__mid">OF MANDALA MAKING WITH</span>
      <span class="title__name">MAREN WHITCOMBE</span>
      <svg class="title__flourish" width="392" height="24" viewBox="0 0 392 24" aria-hidden="true">
        <path d="M0 16 Q100 19 200 15 T 300 14 Q 320 13 322 8 Q 323 2 317 4 Q 312 7 318 14 Q 330 19 392 16" fill="none" stroke="var(--rule)" stroke-width="1.6" stroke-linecap="round"/>
      </svg>
    </h1>

    <div class="class-note">
      <svg width="290" height="300" viewBox="0 0 290 300" aria-hidden="true">
        <path d="M3 4 L262 3 Q272 12 286 22 L287 296 L4 297 Z" fill="none" stroke="var(--rule)" stroke-width="1.7" stroke-linejoin="round"/>
        <path d="M262 3 Q266 16 270 22 Q278 26 286 22" fill="none" stroke="var(--rule)" stroke-width="1.5"/>
      </svg>
      <p class="class-note__label">Next Class will be held:</p>
    </div>

    <p class="web front-web">www.BrightloomandDesigns.com</p>

    <svg class="art art--mandala-half" viewBox="0 0 300 564" role="img" aria-label="Half of a vibrant hand-drawn mandala in orange, red, green, blue and lilac with bold outlines">
      <defs>
        <radialGradient id="mandalaWarm" cx="100%" cy="50%" r="100%">
          <stop offset="0" stop-color="var(--warm-1)"/>
          <stop offset="0.45" stop-color="var(--warm-2)"/>
          <stop offset="0.72" stop-color="var(--lilac)"/>
          <stop offset="0.9" stop-color="var(--cool-2)"/>
          <stop offset="1" stop-color="var(--cool-1)"/>
        </radialGradient>
      </defs>
      <circle cx="330" cy="282" r="318" fill="url(#mandalaWarm)"/>
    </svg>
  </section>

  <section class="postcard postcard--back">
    <svg class="art art--mandala-faint" viewBox="0 0 370 230" role="img" aria-label="Faint grey outline of a mandala pattern in the upper corner">
      <defs>
        <radialGradient id="mandalaFaint" cx="30%" cy="0%" r="90%">
          <stop offset="0" stop-color="var(--faint)"/>
          <stop offset="1" stop-color="#f6f6f6"/>
        </radialGradient>
      </defs>
      <ellipse cx="110" cy="0" rx="260" ry="225" fill="url(#mandalaFaint)"/>
    </svg>

    <svg class="art art--mandala-corner" viewBox="0 0 90 190" role="img" aria-label="Faint grey partial mandala outline at the right edge">
      <ellipse cx="95" cy="95" rx="80" ry="92" fill="#f1f1f1"/>
    </svg>

    <div class="stamp" aria-hidden="true"></div>
    <div class="address-line" style="top:212px"></div>
    <div class="address-line" style="top:252px"></div>
    <div class="address-line" style="top:291px"></div>

    <h2 class="title back-title">
      <span class="title__lead">EXPERIENCE THE MAGIC</span>
      <span class="title__mid">OF MANDALA MAKING WITH</span>
      <span class="title__name">MAREN WHITCOMBE</span>
      <svg class="title__flourish" width="392" height="24" viewBox="0 0 392 24" aria-hidden="true">
        <path d="M0 16 Q100 19 200 15 T 300 14 Q 320 13 322 8 Q 323 2 317 4 Q 312 7 318 14 Q 330 19 392 16" fill="none" stroke="var(--rule)" stroke-width="1.6" stroke-linecap="round"/>
      </svg>
    </h2>

    <p class="visit">VISIT MY WEBSITE AT</p>
    <p class="web back-web">www.BrightloomandDesigns.com</p>
  </section>

</div>
</body>
</html>
```